Tarvik Plans - Worpress Design

We are a consultancy to help builders to optimize their planning in order to save building costs. For that reason we need a website to offer our services, present our history, the mission and offer a plug-in for a first contact (including calendar), testimonials, a blog etc.
As an idea, I really like: https://www.fendrowadvisory.de/
Later on the website should be programmed in www.quelvo.de in our Wordpress area. The text, of course, will be done by myself. The colors should be suitable to our recently designed logo.

```html
<!DOCTYPE html>
<html lang="en">
<head>
<meta charset="utf-8">
<title>Tarvik Plans</title>
<link rel="stylesheet" href="https://fonts.googleapis.com/css2?family=Montserrat:wght@400;500;600;700&display=swap">
<style>
  :root {
    --gold: #c4893a;
    --gold-dark: #a8712a;
    --navy: #1f1d3d;
    --text: #4a4a5a;
    --muted: #7a7a88;
    --white: #ffffff;
    --blush: #fdf0f3;
    --card-blue: #f3f8fd;
    --card-grey: #f4f4f6;
    --footer: #efeff1;
  }
  * { margin: 0; padding: 0; box-sizing: border-box; }
  html, body { width: 1200px; height: 3740px; overflow: hidden; }
  body {
    position: relative;
    background: var(--white);
    font-family: "Montserrat", Arial, sans-serif;
    color: var(--navy);
  }
  .abs { position: absolute; }

  /* header */
  .brand { left: 72px; top: 44px; display: flex; align-items: center; gap: 14px; }
  .brand-mark { width: 34px; height: 34px; background: var(--gold); }
  .brand-name { font-size: 26px; font-weight: 700; color: var(--gold); letter-spacing: 1px; }
  .main-nav { top: 40px; left: 676px; display: flex; gap: 60px; }
  .main-nav a { font-size: 17px; font-weight: 600; color: var(--navy); text-decoration: none; }

  .hero-photo { left: 500px; top: 0; width: 700px; height: 640px; }
  .hero-title { left: 68px; top: 222px; font-size: 66px; font-weight: 700; }
  .hero-text { left: 68px; top: 318px; width: 380px; font-size: 13px; line-height: 20px; color: var(--text); }
  .btn {
    display: inline-flex; align-items: center; justify-content: center;
    height: 40px; border-radius: 20px; font-size: 13px; font-weight: 600; color: var(--white);
  }
  .btn-primary { left: 68px; top: 432px; width: 156px; background: var(--gold); }
  .btn-dark { left: 244px; top: 432px; width: 152px; background: var(--navy); }

  /* consulting */
  .consult-block { left: 68px; top: 700px; width: 170px; height: 472px; background: var(--gold); }
  .consult-card {
    left: 232px; top: 696px; width: 736px; height: 352px;
    background: var(--card-blue); border: 4px solid var(--gold);
  }
  .consult-photo { left: 236px; top: 700px; width: 310px; height: 344px; }
  .consult-title { left: 580px; top: 784px; font-size: 30px; font-weight: 600; }
  .consult-text { left: 580px; top: 842px; width: 340px; font-size: 13px; line-height: 20px; color: var(--text); }
  .learn-more { font-size: 12px; font-weight: 500; color: var(--gold); }
  .consult-more { left: 580px; top: 936px; }

  /* explore */
  .laptop { left: 120px; top: 1340px; width: 460px; height: 280px; }
  .explore-box { left: 428px; top: 1408px; width: 704px; height: 364px; background: var(--gold); }
  .explore-title { left: 692px; top: 1486px; font-size: 36px; font-weight: 700; color: var(--white); }
  .explore-text { left: 692px; top: 1554px; width: 400px; font-size: 12px; line-height: 18px; color: var(--white); }
  .explore-text p + p { margin-top: 12px; }
  .explore-more { left: 692px; top: 1680px; color: var(--white); }

  /* services */
  .blush { left: 0; top: 1790px; width: 1200px; height: 1500px; }
  .section-title { left: 0; width: 1200px; text-align: center; font-weight: 700; }
  .serious-title { top: 1896px; font-size: 40px; }
  .section-text {
    left: 350px; width: 500px; text-align: center; font-size: 13px; line-height: 20px; color: var(--text);
  }
  .serious-text { top: 1976px; }
  .service-card {
    width: 356px; height: 108px; background: var(--card-grey); border-radius: 4px;
    padding: 22px 24px 0 80px;
  }
  .service-icon { position: absolute; left: 24px; top: 22px; width: 32px; height: 28px; border-radius: 4px; }
  .service-card h3 { font-size: 16px; font-weight: 600; margin-bottom: 8px; }
  .service-card p { font-size: 11px; line-height: 16px; color: var(--muted); }

  /* team */
  .team-square { border: 6px solid var(--white); background: var(--gold); }
  .team-title { left: 596px; top: 2616px; font-size: 34px; font-weight: 700; line-height: 48px; }
  .team-text { left: 596px; top: 2740px; width: 380px; font-size: 13px; line-height: 20px; color: var(--text); }
  .team-more { left: 596px; top: 2838px; }

  /* contact */
  .touch-title { top: 3134px; font-size: 38px; line-height: 50px; }
  .btn-contact {
    left: 492px; top: 3272px; width: 216px; height: 66px; border-radius: 33px;
    background: var(--gold); font-size: 22px; color: var(--white);
  }
  .subscribe-title { top: 3434px; font-size: 21px; font-weight: 500; }
  .subscribe-form {
    left: 400px; top: 3512px; width: 400px; height: 40px;
    border: 1px solid var(--gold); border-radius: 20px; overflow: hidden; display: flex;
  }
  .subscribe-form span { flex: 1; padding-left: 18px; font-size: 11px; line-height: 38px; color: var(--muted); }
  .subscribe-form b {
    width: 112px; background: var(--gold); color: var(--white);
    font-size: 12px; font-weight: 600; text-align: center; line-height: 38px; border-radius: 20px;
  }

  .site-footer { left: 0; top: 3684px; width: 1200px; height: 56px; background: var(--footer); }
  .follow { left: 808px; top: 3704px; font-size: 13px; color: var(--text); display: flex; align-items: center; gap: 10px; }
  .social { width: 18px; height: 18px; background: var(--navy); border-radius: 2px; }
</style>
</head>
<body>

<svg class="abs blush" viewBox="0 0 1200 1500" aria-hidden="true">
  <path d="M860 0 C980 40 1200 30 1200 30 L1200 1420 C1000 1500 760 1400 720 1180 C690 1000 820 900 780 700 C740 520 640 420 700 240 C740 110 780 10 860 0 Z" fill="var(--blush)"/>
</svg>

<header>
  <div class="abs brand">
    <span class="brand-mark"></span>
    <span class="brand-name">Tarvik Plans</span>
  </div>
  <nav class="abs main-nav">
    <a href="#">Home</a><a href="#">About</a><a href="#">Services</a><a href="#">Contact</a>
  </nav>
</header>

<svg class="abs hero-photo" viewBox="0 0 700 640" role="img" aria-label="Photo of business people in a meeting around a table">
  <defs>
    <linearGradient id="heroTone" x1="0" y1="0" x2="1" y2="1">
      <stop offset="0" stop-color="#8d8e94"/>
      <stop offset="0.5" stop-color="#56545a"/>
      <stop offset="1" stop-color="#b9a99a"/>
    </linearGradient>
  </defs>
  <path d="M120 0 L700 0 L700 600 C650 620 600 560 540 590 C470 625 420 560 340 570 C280 580 240 520 180 500 C130 480 60 460 90 400 C110 360 40 330 70 280 C95 240 30 200 80 150 C110 120 60 60 120 0 Z" fill="url(#heroTone)"/>
</svg>

<h1 class="abs hero-title">Tarvik Plans</h1>
<p class="abs hero-text">We help builders plan smarter from the first sketch to the final handover. Our consultants review every phase of your project to remove waste, reduce risk and keep your building costs firmly under control.</p>
<span class="abs btn btn-primary">Contact Us</span>
<span class="abs btn btn-dark">View services</span>

<section>
  <div class="abs consult-block"></div>
  <div class="abs consult-card"></div>
  <svg class="abs consult-photo" viewBox="0 0 310 344" role="img" aria-label="Photo of two consultants talking at a desk">
    <defs>
      <linearGradient id="consultTone" x1="0" y1="0" x2="1" y2="1">
        <stop offset="0" stop-color="#d8d2c8"/>
        <stop offset="1" stop-color="#8a6e58"/>
      </linearGradient>
    </defs>
    <rect width="310" height="344" fill="url(#consultTone)"/>
  </svg>
  <h2 class="abs consult-title">Consulting supports</h2>
  <p class="abs consult-text">Independent advice for every stage of planning. We check drawings, schedules and budgets so that your team can build with confidence and avoid costly changes on site.</p>
  <span class="abs learn-more consult-more">Learn More &rarr;</span>
</section>

<section>
  <div class="abs explore-box"></div>
  <svg class="abs laptop" viewBox="0 0 460 280" role="img" aria-label="Laptop showing a photo of a team reviewing plans">
    <defs>
      <linearGradient id="screenTone" x1="0" y1="0" x2="1" y2="1">
        <stop offset="0" stop-color="#a9b4c2"/>
        <stop offset="1" stop-color="#4e5868"/>
      </linearGradient>
    </defs>
    <rect x="60" y="0" width="340" height="250" rx="10" fill="#d7d9dd"/>
    <rect x="72" y="12" width="316" height="226" fill="url(#screenTone)"/>
    <path d="M0 252 L460 252 L440 272 L20 272 Z" fill="#c6c8cc"/>
  </svg>
  <h2 class="abs explore-title">Explore Services</h2>
  <div class="abs explore-text">
    <p>From feasibility studies to tender reviews, our services cover the full planning cycle and are tailored to the size of each project.</p>
    <p>Book a first meeting through our online calendar and learn how a clear plan can lower your costs before the first stone is laid.</p>
  </div>
  <span class="abs learn-more explore-more">Learn More &rarr;</span>
</section>

<section>
  <h2 class="abs section-title serious-title">We Are Serious for Any Project</h2>
  <p class="abs section-text serious-text">Every project deserves careful planning. We work closely with owners, architects and contractors to find savings that last well beyond the day of completion.</p>

  <div class="abs service-card" style="left:232px;top:2100px">
    <span class="service-icon" style="background:#7c8796"></span>
    <h3>Services</h3>
    <p>Detailed cost reviews that show where your budget can be trimmed.</p>
  </div>
  <div class="abs service-card" style="left:608px;top:2100px">
    <span class="service-icon" style="background:#2f2f3a"></span>
    <h3>Services</h3>
    <p>Schedule checks that keep every trade moving in the right order.</p>
  </div>
  <div class="abs service-card" style="left:232px;top:2228px">
    <span class="service-icon" style="background:#4aa6c9"></span>
    <h3>Services</h3>
    <p>Material advice that balances quality, price and delivery times.</p>
  </div>
  <div class="abs service-card" style="left:608px;top:2228px">
    <span class="service-icon" style="background:#e0566a"></span>
    <h3>Services</h3>
    <p>Tender support that helps you compare offers with clear criteria.</p>
  </div>
</section>

<section>
  <div class="abs team-square" style="left:120px;top:2640px;width:260px;height:236px"></div>
  <div class="abs team-square" style="left:300px;top:2688px;width:224px;height:236px"></div>
  <div class="abs team-square" style="left:190px;top:2776px;width:216px;height:188px"></div>
  <h2 class="abs team-title">We Have a Great<br>Team to Work</h2>
  <p class="abs team-text">Our planners, engineers and cost experts bring years of site experience. Together we turn complex projects into clear steps your builders can follow.</p>
  <span class="abs learn-more team-more">Learn More &rarr;</span>
</section>

<section>
  <h2 class="abs section-title touch-title">Get in Touch for Your Project,<br>We will be Happy to Help.</h2>
  <span class="abs btn btn-contact">Contact Us</span>
  <h3 class="abs section-title subscribe-title">Subscribe Us for Updates:</h3>
  <div class="abs subscribe-form"><span>Email address</span><b>SEND</b></div>
</section>

<footer class="abs site-footer"></footer>
<div class="abs follow">Follow Us <span class="social"></span><span class="social"></span><span class="social"></span></div>

</body>
</html>
```